Sailing excursion business needs needs a rolling billboard / minivan wrap

Bramblecrest Sailing based in Treasure Island, Florida needs a wrap for our shuttle van. Our schooner is a local icon and her image is a true feast for the eyes. In addition to the image, please include our web address, BramblecrestSailing.com as well as our telephone number, 727-555-0184.

```html
<!DOCTYPE html>
<html lang="en">
<head>
<meta charset="utf-8">
<title>Bramblecrest Sailing – Shuttle Van Wrap</title>
<link rel="stylesheet" href="https://fonts.googleapis.com/css2?family=Exo+2:ital,wght@0,800;1,900&display=swap">
<style>
  :root {
    --backdrop: #e9ebee;
    --wrap-white: #f7f7f7;
    --wrap-red: #d2141c;
    --wrap-red-deep: #a50d12;
    --wrap-black: #151515;
    --glass: #2b2d31;
    --tyre: #1d1d1f;
    --rim: #b9bcc1;
    --outline: #c9cbcf;
  }
  html, body { margin: 0; padding: 0; overflow: hidden; }
  body { width: 1039px; height: 1200px; background: var(--backdrop); }
  .wrap-sheet { display: block; width: 1039px; height: 1200px; }
  .body-panel { fill: var(--wrap-white); }
  .body-outline { fill: none; stroke: var(--outline); stroke-width: 1.5; }
  .glass { fill: var(--glass); }
  .red { fill: var(--wrap-red); }
  .red-deep { fill: var(--wrap-red-deep); }
  .black { fill: var(--wrap-black); }
  .tyre { fill: var(--tyre); }
  .rim { fill: var(--rim); }
  .lamp { fill: #d9d9d9; }
  .pinstripe { fill: none; stroke: var(--wrap-black); stroke-width: 2; }
  .brand-name { font-family: "Exo 2", sans-serif; font-weight: 800; fill: var(--wrap-black); text-anchor: middle; }
  .phone { font-family: "Exo 2", sans-serif; font-weight: 900; font-style: italic; fill: var(--wrap-red); }
  .web { font-family: "Exo 2", sans-serif; font-weight: 800; fill: var(--wrap-red); }
  .web-dark { fill: var(--wrap-black); }
  .rear-phone { font-family: "Exo 2", sans-serif; font-weight: 800; fill: var(--wrap-red-deep); text-anchor: middle; }
  .rear-web { font-family: "Exo 2", sans-serif; font-weight: 800; text-anchor: middle; }
</style>
</head>
<body>
<svg class="wrap-sheet" viewBox="0 0 1039 1200" xmlns="http://www.w3.org/2000/svg">
  <defs>
    <linearGradient id="schooner-tones" x1="0" y1="0" x2="0" y2="1">
      <stop offset="0" stop-color="#f2f2f2"/>
      <stop offset="0.55" stop-color="#d2141c"/>
      <stop offset="1" stop-color="#1a1a1a"/>
    </linearGradient>
    <radialGradient id="cloud-tones" cx="0.5" cy="0.6" r="0.6">
      <stop offset="0" stop-color="#8d9095"/>
      <stop offset="1" stop-color="#f7f7f7" stop-opacity="0"/>
    </radialGradient>

    <path id="side-body-shape" d="M172,272 Q170,240 200,228 L318,170 Q352,92 430,76 L900,68 Q945,72 958,160 L968,252 L978,262 L976,300 L175,300 Z"/>
    <path id="front-body-shape" d="M150,1150 L128,1040 Q120,960 150,900 L180,845 Q310,830 440,845 L470,900 Q500,960 492,1040 L470,1150 Z"/>
    <path id="rear-body-shape" d="M580,1150 L565,1020 Q562,910 590,850 Q750,832 910,850 Q938,910 935,1020 L920,1150 Z"/>

    <clipPath id="side-body-clip"><use href="#side-body-shape"/></clipPath>
    <clipPath id="front-body-clip"><use href="#front-body-shape"/></clipPath>
    <clipPath id="rear-body-clip"><use href="#rear-body-shape"/></clipPath>

    <g id="side-wrap">
      <use href="#side-body-shape" class="body-panel"/>
      <g class="side-graphics" clip-path="url(#side-body-clip)">
        <path class="glass" d="M352,166 Q385,96 440,86 L555,84 L555,170 Z"/>
        <rect class="glass" x="565" y="82" width="175" height="88" rx="6"/>
        <path class="glass" d="M750,82 L885,80 Q915,82 922,150 L924,168 L750,170 Z"/>
        <path class="black" d="M895,250 L985,250 L985,310 L900,310 Z"/>
        <path class="red" d="M170,268 Q190,232 260,220 Q330,210 400,205 L375,235 Q300,232 262,250 Q230,270 222,300 L170,300 Z"/>
        <path class="red-deep" d="M555,232 Q600,300 665,305 Q725,300 745,230 L745,312 L560,312 Z"/>
        <path class="red" d="M745,232 Q790,220 850,222 Q905,226 930,250 L920,275 Q880,240 830,245 Q790,250 775,300 L750,310 Z"/>
        <path class="pinstripe" d="M720,300 L740,232 M730,302 L748,240 M930,250 L945,300"/>
        <rect x="560" y="172" width="170" height="38" fill="url(#cloud-tones)" role="img" aria-label="Soft grey cloud graphic"/>
        <rect x="380" y="190" width="165" height="110" rx="55" fill="url(#schooner-tones)" role="img" aria-label="Schooner with red sails on the water inside an arched frame"/>
      </g>
      <use href="#side-body-shape" class="body-outline"/>
      <circle class="tyre" cx="292" cy="300" r="58"/>
      <circle class="rim" cx="292" cy="300" r="36"/>
      <circle class="tyre" cx="812" cy="300" r="58"/>
      <circle class="rim" cx="812" cy="300" r="36"/>
    </g>
  </defs>

  <g class="van-side van-side--left">
    <use href="#side-wrap"/>
    <text class="brand-name" x="650" y="240" font-size="24" textLength="160" lengthAdjust="spacingAndGlyphs">BRAMBLECREST</text>
    <text class="brand-name" x="650" y="262" font-size="17">·SAILING·</text>
    <text class="phone" x="750" y="192" font-size="22">727-555-0184</text>
    <text class="web" x="750" y="216" font-size="12" textLength="180" lengthAdjust="spacingAndGlyphs">BRAMBLECRESTSAILING.COM</text>
  </g>

  <g class="van-side van-side--right">
    <use href="#side-wrap" transform="translate(1039,385) scale(-1,1)"/>
    <text class="brand-name" x="393" y="625" font-size="24" textLength="160" lengthAdjust="spacingAndGlyphs">BRAMBLECREST</text>
    <text class="brand-name" x="393" y="647" font-size="17">·SAILING·</text>
    <text class="phone" x="112" y="577" font-size="22">727-555-0184</text>
    <text class="web" x="112" y="601" font-size="12" textLength="180" lengthAdjust="spacingAndGlyphs">BRAMBLECRESTSAILING.COM</text>
  </g>

  <g class="van-front">
    <use href="#front-body-shape" class="body-panel"/>
    <g class="front-graphics" clip-path="url(#front-body-clip)">
      <path class="glass" d="M165,915 L192,852 Q310,840 428,852 L455,915 Q310,925 165,915 Z"/>
      <rect x="240" y="930" width="140" height="44" rx="22" fill="url(#schooner-tones)" role="img" aria-label="Schooner emblem with red sails"/>
      <rect class="black" x="215" y="1028" width="190" height="38" rx="8"/>
      <rect class="lamp" x="140" y="1030" width="70" height="22" rx="8"/>
      <rect class="lamp" x="410" y="1030" width="70" height="22" rx="8"/>
      <path class="red" d="M100,1090 Q310,1080 520,1090 L520,1140 Q310,1150 100,1140 Z"/>
      <rect class="black" x="195" y="1100" width="230" height="24" rx="6"/>
    </g>
    <use href="#front-body-shape" class="body-outline"/>
    <rect class="black" x="118" y="905" width="30" height="20" rx="6"/>
    <rect class="black" x="472" y="905" width="30" height="20" rx="6"/>
    <text class="brand-name" x="310" y="996" font-size="17" textLength="150" lengthAdjust="spacingAndGlyphs">BRAMBLECREST</text>
    <text class="brand-name" x="310" y="1012" font-size="11">·SAILING·</text>
  </g>

  <g class="van-rear">
    <use href="#rear-body-shape" class="body-panel"/>
    <g class="rear-graphics" clip-path="url(#rear-body-clip)">
      <rect x="785" y="870" width="100" height="65" rx="32" fill="url(#schooner-tones)" role="img" aria-label="Schooner with red sails inside an arched frame"/>
      <path class="red" d="M560,968 Q650,935 720,950 Q790,968 860,945 Q905,935 940,965 L940,985 L560,985 Z"/>
      <path class="red-deep" d="M560,985 L700,985 L700,1012 L560,1012 Z M800,985 L940,985 L940,1012 L800,1012 Z"/>
      <rect x="718" y="982" width="64" height="34" rx="3" fill="#cfd2d6"/>
      <rect x="735" y="990" width="30" height="16" fill="#e04a4f"/>
      <path class="black" d="M560,1092 L940,1092 L940,1155 L560,1155 Z"/>
    </g>
    <use href="#rear-body-shape" class="body-outline"/>
    <text class="brand-name" x="695" y="905" font-size="23" textLength="160" lengthAdjust="spacingAndGlyphs">BRAMBLECREST</text>
    <text class="brand-name" x="695" y="926" font-size="15">·SAILING·</text>
    <text class="rear-phone" x="750" y="1052" font-size="22">727-555-0184</text>
    <text class="rear-web" x="750" y="1081" font-size="15" textLength="250" lengthAdjust="spacingAndGlyphs"><tspan class="web-dark">BRAMBLECREST</tspan><tspan fill="#d2141c">SAILING</tspan><tspan class="web-dark">.COM</tspan></text>
  </g>
</svg>
</body>
</html>
```